Roof wash and Gutter Cleaning

Would like to see our colors and logo incorporated into design along with phone number and before/after picture(s). We use a non pressure softwash process we use unlike high pressure. We are a exterior cleaning company that likes to set our standards high with safe methods to cleaning the everyday surfaces on homes.
“Serving the Tri-State Area”
A list of our services:
House washing
Shingle and metal roof washing
Deck cleaning
Window cleaning
Concrete cleaning
Gutter cleaning
415-362-0917
We do not need the address section as these will be more for our meet and greets. As well handed out as clipped door  postcards.

Target Market(s)
Shingle roof wash and gutter cleaning
Look and feel

```html
<!DOCTYPE html>
<html lang="en">
<head>
<meta charset="utf-8">
<title>Summit Exterior Cleaning – Postcard</title>
<link href="https://fonts.googleapis.com/css2?family=Montserrat:wght@700&family=Ubuntu:wght@400;500;700&display=swap" rel="stylesheet">
<style>
  :root {
    --page-bg: #e2e2e2;
    --card-bg: #ffffff;
    --brand-green: #4bb33a;
    --brand-blue: #3a6fb0;
    --heading-blue: #2f6ab3;
    --ink: #1d1d1d;
    --ring-green: #52b846;
    --service-step: 64.6px;
  }
  * { margin: 0; padding: 0; box-sizing: border-box; }
  html, body {
    width: 1200px; height: 904px; overflow: hidden;
    background: var(--page-bg);
  }
  .postcard {
    position: absolute; left: 0; top: 52px;
    width: 1200px; height: 800px;
    background: var(--card-bg);
    overflow: hidden;
    font-family: "Ubuntu", sans-serif;
  }
  .photo-grid { position: absolute; inset: 0; width: 1200px; height: 800px; }
  .photo-label {
    font-family: "Ubuntu", sans-serif; font-weight: 500; font-size: 21px;
    fill: #ffffff;
    filter: drop-shadow(1px 1px 1.5px rgba(0,0,0,0.75));
  }
  .brand {
    position: absolute; left: 28px; top: 42px; width: 300px;
    text-align: center; color: var(--brand-blue);
  }
  .brand-name {
    font-family: "Ubuntu", sans-serif; font-weight: 700; font-size: 54px;
    line-height: 1; letter-spacing: 1px;
  }
  .brand-sub {
    font-family: "Ubuntu", sans-serif; font-weight: 700; font-size: 12px;
    margin-top: 22px; letter-spacing: 0.3px;
  }
  .area-band {
    position: absolute; left: 0; top: 179px; width: 368px; height: 111px;
    background: var(--brand-green);
    clip-path: polygon(0 0, 350px 0, 368px 111px, 0 111px);
    color: #fff;
    font-family: "Montserrat", sans-serif; font-weight: 700;
    font-size: 37px; line-height: 47px; letter-spacing: 1px;
    padding: 8px 0 0 42px;
  }
  .services { position: absolute; left: 42px; top: 306px; width: 340px; height: 420px; }
  .services-title {
    font-weight: 700; font-size: 27px; color: var(--heading-blue);
    letter-spacing: 0.2px;
  }
  .service-list { list-style: none; position: absolute; left: 4px; top: 35px; }
  .service {
    position: absolute; left: 0;
    display: flex; align-items: center; gap: 16px;
    width: 320px; height: 56px;
    font-size: 24px; line-height: 29px; color: var(--ink);
    white-space: nowrap;
  }
  .service:nth-child(1) { top: calc(var(--service-step) * 0); }
  .service:nth-child(2) { top: calc(var(--service-step) * 1); }
  .service:nth-child(3) { top: calc(var(--service-step) * 2); }
  .service:nth-child(4) { top: calc(var(--service-step) * 3); }
  .service:nth-child(5) { top: calc(var(--service-step) * 4); }
  .service:nth-child(6) { top: calc(var(--service-step) * 5); }
  .service-icon {
    flex: none; width: 56px; height: 56px; border-radius: 50%;
    background: var(--brand-blue);
    border: 3px solid var(--ring-green);
    box-shadow: inset 0 0 0 2px #fff;
    display: flex; align-items: center; justify-content: center;
  }
  .service-icon svg { width: 30px; height: 30px; }
  .call-bar {
    position: absolute; left: 0; top: 734px; width: 477px; height: 66px;
    background: var(--brand-blue);
    clip-path: polygon(0 0, 465px 0, 477px 66px, 0 66px);
    display: flex; align-items: center; gap: 16px;
    padding-left: 46px; color: #fff;
    font-weight: 700; font-size: 31px; letter-spacing: 0.3px;
  }
  .call-bar svg { width: 32px; height: 32px; }
  .call-number { display: flex; align-items: center; gap: 10px; }
</style>
</head>
<body>
<main class="postcard">

  <svg class="photo-grid" viewBox="0 0 1200 800">
    <defs>
      <linearGradient id="roofGrey" x1="0" y1="0" x2="0" y2="1">
        <stop offset="0" stop-color="#6c6a5e"/>
        <stop offset="0.3" stop-color="#8a8478"/>
        <stop offset="1" stop-color="#5c5a52"/>
      </linearGradient>
      <linearGradient id="roofGreyClean" x1="0" y1="0" x2="0" y2="1">
        <stop offset="0" stop-color="#72705f"/>
        <stop offset="0.3" stop-color="#9d978a"/>
        <stop offset="1" stop-color="#7d776d"/>
      </linearGradient>
      <linearGradient id="roofRedDirty" x1="0" y1="0" x2="1" y2="1">
        <stop offset="0" stop-color="#7c5446"/>
        <stop offset="0.6" stop-color="#8f7f72"/>
        <stop offset="1" stop-color="#6a4a3e"/>
      </linearGradient>
      <linearGradient id="roofRed" x1="0" y1="0" x2="1" y2="1">
        <stop offset="0" stop-color="#8a6152"/>
        <stop offset="1" stop-color="#a35f4c"/>
      </linearGradient>
      <linearGradient id="gutterDirty" x1="0" y1="0" x2="1" y2="1">
        <stop offset="0" stop-color="#5b5c60"/>
        <stop offset="0.5" stop-color="#7b6046"/>
        <stop offset="1" stop-color="#4d4036"/>
      </linearGradient>
      <linearGradient id="gutterClean" x1="0" y1="0" x2="1" y2="1">
        <stop offset="0" stop-color="#5d5e63"/>
        <stop offset="0.5" stop-color="#9a9784"/>
        <stop offset="1" stop-color="#6b4b34"/>
      </linearGradient>
      <linearGradient id="houseScene" x1="0" y1="0" x2="0" y2="1">
        <stop offset="0" stop-color="#8a8a86"/>
        <stop offset="0.35" stop-color="#6e5346"/>
        <stop offset="0.65" stop-color="#d8cfaa"/>
        <stop offset="1" stop-color="#3f5634"/>
      </linearGradient>
      <linearGradient id="arrowFill" x1="0" y1="0" x2="1" y2="0">
        <stop offset="0" stop-color="#4bb33a"/>
        <stop offset="1" stop-color="#3a7ab8"/>
      </linearGradient>
      <symbol id="arrow" viewBox="0 0 56 28">
        <polygon points="0,8 34,8 34,0 56,14 34,28 34,20 0,20" fill="url(#arrowFill)" stroke="#ffffff" stroke-width="1.2"/>
      </symbol>
    </defs>

    <g role="img" aria-label="Before photo: grey shingle roof with vent pipe, covered in moss and fallen leaves">
      <polygon points="321,0 756,0 807,266 376,266" fill="url(#roofGrey)"/>
    </g>
    <g role="img" aria-label="After photo: the same grey shingle roof cleaned">
      <polygon points="762,0 1200,0 1200,266 813,266" fill="url(#roofGreyClean)"/>
    </g>

    <g role="img" aria-label="Before photo: red shingle roof valley full of debris">
      <polygon points="376,273 598,273 643,531 426,531" fill="url(#roofRedDirty)"/>
    </g>
    <g role="img" aria-label="After photo: the red shingle roof valley cleaned">
      <polygon points="604,273 809,273 854,531 649,531" fill="url(#roofRed)"/>
    </g>
    <g role="img" aria-label="Before photo: gutter clogged with leaves">
      <polygon points="815,273 1026,273 1068,531 860,531" fill="url(#gutterDirty)"/>
    </g>
    <g role="img" aria-label="After photo: the same gutter cleared">
      <polygon points="1032,273 1200,273 1200,531 1074,531" fill="url(#gutterClean)"/>
    </g>

    <g role="img" aria-label="Before photo: two-storey house with brown roof and white porch">
      <polygon points="431,539 866,539 916,800 477,800" fill="url(#houseScene)"/>
    </g>
    <g role="img" aria-label="After photo: the same house with its roof cleaned">
      <polygon points="872,539 1200,539 1200,800 922,800" fill="url(#houseScene)"/>
    </g>

    <text class="photo-label" x="646" y="58">Before</text>
    <use href="#arrow" x="742" y="38" width="56" height="28"/>
    <text class="photo-label" x="1052" y="58">After</text>

    <text class="photo-label" x="500" y="302">Before</text>
    <use href="#arrow" x="579" y="285" width="46" height="23"/>
    <text class="photo-label" x="749" y="302">After</text>
    <text class="photo-label" x="932" y="302">Before</text>
    <use href="#arrow" x="1010" y="285" width="46" height="23"/>
    <text class="photo-label" x="1130" y="302">After</text>

    <text class="photo-label" x="802" y="775">Before</text>
    <use href="#arrow" x="895" y="753" width="58" height="29"/>
    <text class="photo-label" x="1130" y="775">After</text>
  </svg>

  <header class="brand">
    <div class="brand-name">Summit</div>
    <div class="brand-sub">Exterior Cleaning &amp; Maintenance Co.</div>
  </header>

  <div class="area-band">Serving the<br>Tri-State Area</div>

  <section class="services">
    <h2 class="services-title">OUR SERVICES:</h2>
    <ul class="service-list">
      <li class="service">
        <span class="service-icon"><svg viewBox="0 0 30 30" fill="none" stroke="#fff" stroke-width="1.6"><path d="M5 14 L15 5 L25 14"/><rect x="8" y="13" width="14" height="12"/><rect x="12" y="18" width="5" height="7"/></svg></span>
        <span>House washing</span>
      </li>
      <li class="service">
        <span class="service-icon"><svg viewBox="0 0 30 30" fill="none" stroke="#fff" stroke-width="1.6"><path d="M4 20 L9 9 H21 L26 20 Z"/><path d="M6 16 H24 M7 12 H23 M12 9 L11 20 M18 9 L19 20"/></svg></span>
        <span>Shingle and metal<br>roof washing</span>
      </li>
      <li class="service">
        <span class="service-icon"><svg viewBox="0 0 30 30" fill="none" stroke="#fff" stroke-width="1.6"><path d="M4 16 H26 M4 21 H26 M7 16 V26 M15 16 V26 M23 16 V26 M7 16 V8 M23 16 V8 M7 10 H23"/></svg></span>
        <span>Deck cleaning</span>
      </li>
      <li class="service">
        <span class="service-icon"><svg viewBox="0 0 30 30" fill="none" stroke="#fff" stroke-width="1.6"><path d="M6 24 L17 13 M14 10 L20 16 M17 7 L23 13"/><path d="M22 5 L25 8 M20 4 V6 M26 10 H24"/></svg></span>
        <span>Window cleaning</span>
      </li>
      <li class="service">
        <span class="service-icon"><svg viewBox="0 0 30 30" fill="none" stroke="#fff" stroke-width="1.6"><rect x="8" y="6" width="14" height="12" rx="2"/><path d="M11 12 H19 M15 18 V25 M9 25 H21"/></svg></span>
        <span>Concrete cleaning</span>
      </li>
      <li class="service">
        <span class="service-icon"><svg viewBox="0 0 30 30" fill="none" stroke="#fff" stroke-width="1.6"><path d="M4 8 L24 14 M6 14 H24 V18 H6 Z M20 18 V26 M16 26 H24"/></svg></span>
        <span>Gutter cleaning</span>
      </li>
    </ul>
  </section>

  <footer class="call-bar">
    <span>CALL US</span>
    <span class="call-number">
      <svg viewBox="0 0 32 32" fill="none" stroke="#fff" stroke-width="2"><circle cx="16" cy="16" r="13"/><path d="M11 9 L14 9 L15 13 L13 14.5 C14 17 15 18 17.5 19 L19 17 L23 18 L23 21 C23 22 22 23 21 23 C15 22.5 9.5 17 9 11 C9 10 10 9 11 9 Z" fill="#fff" stroke="none"/></svg>
      (415) 362-0917
    </span>
  </footer>

</main>
</body>
</html>
```